New Solo Law Office Needs Business Card/Letterhead Design

I am starting a solo law office called "Law Office of Brian Kolmer, PLLC" in Tucson, Arizona. I will be doing criminal defense trial work. More than a logo with any sort of icon, I am really just looking for the name of the company to be displayed in a sleek, minimalist but interesting sort of way, with a format and font type that communicates professionalism. It can be in color, but doesn't have to be, and I am thinking blue and/or red accents colors. I'd like it to convey that I am passionate, dependable and willing to fight. For the business card, I envision sort of higher quality card material, and maybe some embossing or raised print. I will want to include my company name, name, phone and fax numbers, email and website addresses. For the letterhead, I will want to be able to use the same sort of font/formatting design as on the business card.
Industry/Entity Type
Business
Contact Information for Business Card
Law Office of Brian Kolmer, PLLC
Brian Kolmer
brian@kolmer-law.example
www.kolmer-law.example
(I do not yet have an established phone or fax number, so please put in some place holder numbers for the formatting, and I can add the actual numbers in before I print.)
Colors
Designer to choose colors to be used in the design.
Look and feel
Each slider illustrates characteristics of the customer's brand and the style your logo design should communicate.

```html
<!DOCTYPE html>
<html lang="en">
<head>
<meta charset="utf-8">
<title>Law Office of Brian Kolmer, PLLC — Business Card</title>
<link href="https://fonts.googleapis.com/css2?family=Cinzel:wght@400;500&family=Open+Sans:wght@400;700&display=swap" rel="stylesheet">
<style>
  :root {
    --stage: #111111;
    --paper: #e4e4e4;
    --paper-light: #f1f1f1;
    --paper-shade: #c9c9c9;
    --ink: #0d0d0d;
    --ink-soft: #1c1c1c;
    --silver: #d8d8d8;
    --white: #ffffff;
    --label: #ffffff;
  }
  * { box-sizing: border-box; margin: 0; padding: 0; }
  html, body {
    width: 1200px; height: 1200px; overflow: hidden;
    background: var(--stage);
  }
  .sheet {
    position: relative; width: 1200px; height: 1200px;
  }
  .card {
    position: absolute; left: 170px; width: 860px; height: 480px;
    background: linear-gradient(160deg, var(--paper-light), var(--paper) 55%, var(--paper-shade));
    overflow: hidden;
  }
  .card--back { top: 40px; }
  .card--front { top: 620px; }
  .card svg { position: absolute; inset: 0; }
  .side-label {
    position: absolute; left: 0; width: 1200px; text-align: center;
    font-family: "Open Sans", sans-serif; font-weight: 700; font-size: 40px;
    color: var(--label); letter-spacing: 2px;
  }
  .side-label--back { top: 532px; }
  .side-label--front { top: 1112px; }

  /* back */
  .back-title {
    position: absolute; left: 0; width: 860px; top: 218px; text-align: center;
    font-family: "Cinzel", serif; font-size: 29px; color: var(--silver);
    letter-spacing: 0.5px;
  }
  .back-url {
    position: absolute; left: 0; width: 860px; top: 268px; text-align: center;
    font-family: "Open Sans", sans-serif; font-size: 19px; color: var(--silver);
    letter-spacing: 1.5px;
  }

  /* front */
  .firm-block {
    position: absolute; left: 20px; width: 330px; top: 165px; text-align: center;
    font-family: "Open Sans", sans-serif; color: var(--ink);
  }
  .firm-name { font-weight: 700; font-size: 27px; line-height: 35px; }
  .firm-url { margin-top: 14px; font-size: 19px; letter-spacing: 1.5px; }
  .person-block {
    position: absolute; left: 420px; width: 400px; top: 185px; text-align: center;
    color: var(--white);
  }
  .person-name {
    font-family: "Cinzel", serif; font-size: 40px; letter-spacing: 1px; line-height: 48px;
  }
  .person-rule {
    height: 1px; margin: 6px auto 8px; width: 380px;
    background: linear-gradient(90deg, transparent, #9a9a9a 30%, #9a9a9a 70%, transparent);
  }
  .contact-list { list-style: none; font-family: "Open Sans", sans-serif; font-size: 22px; line-height: 30px; }
  .contact-list li { display: flex; justify-content: center; align-items: center; gap: 10px; }
  .contact-list svg { position: static; width: 20px; height: 20px; flex: none; }
</style>
</head>
<body>
<main class="sheet">

  <section class="card card--back" aria-label="Card back">
    <svg viewBox="0 0 860 480" width="860" height="480" aria-hidden="true">
      <defs>
        <linearGradient id="bandBack" x1="0" y1="0" x2="0" y2="1">
          <stop offset="0" stop-color="#050505"/>
          <stop offset="0.5" stop-color="#1a1a1a"/>
          <stop offset="1" stop-color="#060606"/>
        </linearGradient>
      </defs>
      <path d="M0,132 C180,72 380,72 560,112 S800,152 860,142 L860,160 C780,168 700,150 560,130 S180,92 0,150 Z" fill="#a9a9a9"/>
      <path d="M0,140 C180,80 380,80 560,120 S800,160 860,150 L860,390 C700,450 520,432 330,402 S80,375 0,382 Z" fill="url(#bandBack)"/>
      <path d="M0,382 C80,375 200,385 330,402 S700,450 860,390 L860,400 C700,462 520,442 330,412 S80,385 0,392 Z" fill="#b5b5b5"/>
    </svg>
    <p class="back-title">LAW OFFICE OF BRIAN KOLMER, PLLC</p>
    <p class="back-url">www.kolmer-law.example</p>
  </section>
  <p class="side-label side-label--back">back</p>

  <section class="card card--front" aria-label="Card front">
    <svg viewBox="0 0 860 480" width="860" height="480" aria-hidden="true">
      <defs>
        <linearGradient id="bandFront" x1="0" y1="0" x2="0" y2="1">
          <stop offset="0" stop-color="#060606"/>
          <stop offset="0.45" stop-color="#1b1b1b"/>
          <stop offset="1" stop-color="#050505"/>
        </linearGradient>
      </defs>
      <path d="M364,0 C330,60 330,200 345,300 C355,380 385,440 370,480 L860,480 L860,0 Z" fill="url(#bandFront)"/>
      <line x1="345" y1="140" x2="860" y2="140" stroke="#2a2a2a" stroke-width="2"/>
      <line x1="350" y1="400" x2="860" y2="400" stroke="#242424" stroke-width="2"/>
    </svg>
    <div class="firm-block">
      <p class="firm-name">Law Office<br>of<br>Brian Kolmer, PLLC</p>
      <p class="firm-url">www.kolmer-law.example</p>
    </div>
    <div class="person-block">
      <p class="person-name">Brian Kolmer</p>
      <div class="person-rule"></div>
      <ul class="contact-list">
        <li>
          <svg viewBox="0 0 20 20" aria-label="Email"><rect x="2" y="5" width="16" height="11" fill="none" stroke="#fff" stroke-width="1.4"/><path d="M2 5 L10 11 L18 5 M2 16 L8 10 M18 16 L12 10" fill="none" stroke="#fff" stroke-width="1.2"/></svg>
          <span>brian@kolmer-law.example</span>
        </li>
        <li>
          <svg viewBox="0 0 20 20" aria-label="Phone"><rect x="6" y="2" width="9" height="16" rx="1.5" fill="none" stroke="#fff" stroke-width="1.6"/><line x1="9" y1="15" x2="12" y2="15" stroke="#fff" stroke-width="1.4"/></svg>
          <span>000 5550 1234</span>
        </li>
        <li>
          <svg viewBox="0 0 20 20" aria-label="Fax"><rect x="5" y="3" width="10" height="5" fill="#fff"/><rect x="2" y="8" width="16" height="8" rx="1.5" fill="#fff"/><rect x="6" y="12" width="8" height="5" fill="#111"/></svg>
          <span>000 5550 1234</span>
        </li>
      </ul>
    </div>
  </section>
  <p class="side-label side-label--front">front</p>

</main>
</body>
</html>
```